card for handyman and landscaping business, double sided with services listed on the back

Design a business card for a handyman and Landscaping business in San Jose,ca. Would like front to be a house with 3D characters doing different tasks i.e. Mowing lawn, painting, sprinklers, lighting, weed whacking, power washing, lumber etc. on the backside a cutout of the interior with computer, internet, cleaning, bathroom/kitchen remodeling, smart home etc.

Industry/Entity Type

Handyman

Contact Information for Business Card

Two sided view of a house, one outside services and one inside services

Colors

Designer to choose colors to be used in the design.

Requirements
Must have
• General Household Repairs and Maintenance
• Landscaping, Gardening, and Planting
• Painting, Patching and Trim/Moulding Work
• Cleaning, Restoring and Hauling/Trash Removal
• Blinds, Curtains, and Assembly Work
• Computer, Internet/Wireless, and Smart Home Service

```html
<!DOCTYPE html>
<html lang="en">
<head>
<meta charset="utf-8">
<title>Handyman &amp; Landscaping Business Card</title>
<link rel="stylesheet" href="https://fonts.googleapis.com/css2?family=Arimo:wght@400;700&family=Archivo+Black&display=swap">
<style>
  :root {
    --page-bg: #e9e7e2;
    --green-light: #4caf47;
    --green-dark: #1f9e45;
    --green-ink: #1d6b2f;
    --yellow: #fbbd14;
    --white: #ffffff;
    --art-tone-a: #8fbf5a;
    --art-tone-b: #c9dca6;
  }
  * { box-sizing: border-box; margin: 0; padding: 0; }
  html, body { width: 1200px; height: 1200px; overflow: hidden; }
  body {
    background: var(--page-bg);
    font-family: "Arimo", Arial, sans-serif;
    position: relative;
  }
  .card {
    position: absolute;
    left: 250px;
    width: 700px;
    height: 400px;
    overflow: hidden;
    box-shadow: 0 6px 18px rgba(0,0,0,0.18);
  }
  .card--front {
    top: 130px;
    background: linear-gradient(135deg, var(--green-light) 0%, var(--green-dark) 100%);
    color: var(--white);
  }
  .card--back {
    top: 670px;
    background: var(--white);
  }

  /* Front */
  .front-mascot {
    position: absolute;
    left: 60px;
    top: 105px;
    width: 170px;
    height: 160px;
    border-radius: 10px;
    background: linear-gradient(160deg, var(--art-tone-b) 0%, var(--art-tone-a) 100%);
  }
  .brand {
    position: absolute;
    left: 245px;
    top: 96px;
    white-space: nowrap;
  }
  .brand__kicker {
    display: block;
    font-size: 13px;
    letter-spacing: 0.5px;
    margin-left: 150px;
    margin-bottom: 2px;
  }
  .brand__name {
    font-family: "Archivo Black", "Arial Black", sans-serif;
    font-size: 36px;
    font-weight: 400;
    line-height: 1.08;
    letter-spacing: 0.3px;
  }
  .brand__name span { display: block; }
  .brand__name span + span { padding-left: 58px; }
  .front-services {
    position: absolute;
    left: 30px;
    right: 30px;
    bottom: 42px;
    text-align: center;
    font-size: 17px;
    line-height: 1.6;
  }

  /* Back */
  .back-panel {
    position: absolute;
    top: 0;
    right: 0;
    width: 420px;
    height: 400px;
    background: linear-gradient(135deg, var(--green-light) 0%, var(--green-dark) 100%);
  }
  .back-mascot {
    position: absolute;
    left: 30px;
    top: 40px;
    width: 220px;
    height: 320px;
    border-radius: 10px;
    background: linear-gradient(160deg, var(--art-tone-b) 0%, var(--art-tone-a) 100%);
  }
  .name-band {
    position: absolute;
    top: 40px;
    right: 0;
    width: 440px;
    height: 62px;
    background: var(--yellow);
    display: flex;
    align-items: center;
    justify-content: flex-end;
    padding-right: 26px;
    color: var(--green-ink);
  }
  .name-band__name {
    font-family: "Archivo Black", "Arial Black", sans-serif;
    font-size: 30px;
  }
  .name-band__rule {
    width: 2px; height: 32px; background: var(--green-ink);
    margin: 0 12px;
  }
  .name-band__role { font-size: 22px; }
  .contact-list, .service-list {
    position: absolute;
    list-style: none;
    text-align: right;
    color: var(--white);
  }
  .contact-list { top: 122px; right: 26px; font-size: 18px; line-height: 1.6; }
  .contact-list li { display: flex; align-items: center; justify-content: flex-end; gap: 10px; }
  .contact-list svg { width: 14px; height: 14px; flex: none; }
  .service-list { top: 262px; right: 50px; font-size: 19px; line-height: 1.45; }
</style>
</head>
<body>

<section class="card card--front" aria-label="Card front">
  <div class="front-mascot" role="img" aria-label="Cartoon gardener pushing a lawn mower"></div>
  <div class="brand">
    <span class="brand__kicker">BUSINESS</span>
    <h1 class="brand__name"><span>HANDYMAN &amp;</span><span>LANDSCAPING</span></h1>
  </div>
  <p class="front-services">
    Cleaning, Bath/Kitchen, Baseboards/Trim/Moulding, Smart Home<br>
    A/C and Heating, Blinds, Curtains, Assembly Services, Computer/Tech Service
  </p>
</section>

<section class="card card--back" aria-label="Card back">
  <div class="back-panel"></div>
  <div class="back-mascot" role="img" aria-label="Cartoon gardener in overalls pushing a lawn mower"></div>
  <div class="name-band">
    <span class="name-band__name">JOHN DOE</span>
    <span class="name-band__rule"></span>
    <span class="name-band__role">Director</span>
  </div>
  <ul class="contact-list">
    <li>1-234-567890
      <svg viewBox="0 0 16 16" aria-hidden="true"><path fill="#24352a" d="M3 2l3 0 1 3-2 1.5c1 2 2.5 3.5 4.5 4.5L11 9l3 1v3c0 1-1 1.5-2 1.5C6 14 2 10 1.5 4 1.5 3 2 2 3 2z"/></svg></li>
    <li>www.companyname.com
      <svg viewBox="0 0 16 16" aria-hidden="true"><circle cx="8" cy="8" r="6.5" fill="none" stroke="#24352a" stroke-width="1.6"/><path d="M1.5 8h13M8 1.5c-3 3.5-3 9.5 0 13M8 1.5c3 3.5 3 9.5 0 13" fill="none" stroke="#24352a" stroke-width="1.2"/></svg></li>
    <li>john@companyname.com
      <svg viewBox="0 0 16 16" aria-hidden="true"><rect x="1" y="3" width="14" height="10" fill="#24352a"/><path d="M1 3l7 6 7-6" fill="none" stroke="#4caf47" stroke-width="1.2"/></svg></li>
    <li>Dummy city, Dummy Country Land
      <svg viewBox="0 0 16 16" aria-hidden="true"><path fill="#24352a" d="M8 1a5 5 0 0 1 5 5c0 4-5 9-5 9S3 10 3 6a5 5 0 0 1 5-5z"/><circle cx="8" cy="6" r="1.8" fill="#fbbd14"/></svg></li>
  </ul>
  <ul class="service-list">
    <li>Handyman | Landscaping</li>
    <li>Sprinklers/Irrigation | Painting</li>
    <li>Electrical | Lighting</li>
    <li>Power Washing | Hauling</li>
  </ul>
</section>

</body>
</html>
```